Email Marketing Campaign Templates

Email drip childcare campaign designed to communicate with parents interested in services. We would like the template(s) to be created so that we can change the content as needed.I will add below collateral that we have used in the past as well as logo.
three to for templates 1.) welcome template 2/ things to bring 3) generic template
Target Market(s)
Parents and Millennials
Industry/Entity Type
Childcare
Colors
85cae6
0493ce
9bcb3c
add136
fefefe
faa54b
cadf82
86cae7
33a6d7
Requirements
Must have
- Photos of staff with children
Nice to have
- Photos

```html
<!DOCTYPE html>
<html lang="en">
<head>
<meta charset="utf-8">
<title>Bloom Early Learning Center | Email Marketing 2/3</title>
<link rel="stylesheet" href="https://fonts.googleapis.com/css2?family=Indie+Flower&family=Lato:wght@400;700&display=swap">
<style>
  :root{
    --page:#f2f2f2;
    --paper:#fbfbf8;
    --ink:#1e1e1e;
    --sky:#16c1f0;
    --sky-deep:#33a6d7;
    --orange:#faa54b;
    --green:#9bcb3c;
    --green-light:#add136;
    --white:#fefefe;
  }
  *{box-sizing:border-box;margin:0;padding:0}
  html,body{width:1200px;height:930px;overflow:hidden;background:var(--page)}
  body{position:relative;font-family:"Lato",Arial,sans-serif;color:var(--ink)}

  .sheet-header{position:absolute;left:101px;top:60px;font-size:16px;letter-spacing:.2px}
  .sheet-header strong{font-weight:700}
  .sheet-rule{position:absolute;left:102px;top:90px;width:997px;height:1px;background:var(--ink)}

  .email{position:absolute;top:124px;width:476px;height:766px;background:var(--paper);
    box-shadow:0 1px 4px rgba(0,0,0,.12);overflow:hidden}
  .email--bring{left:102px}
  .email--welcome{left:623px}
  .email__art{position:absolute;inset:0;width:476px;height:766px}

  .brand{position:absolute;left:50px;top:150px;display:flex;align-items:center;gap:10px}
  .brand__dot{width:22px;height:22px;border-radius:50%;background:var(--green)}
  .brand__name{font-family:"Lato",Arial,sans-serif;font-weight:700;font-size:26px;color:var(--sky-deep);line-height:1.05}

  .headline{position:absolute;left:237px;top:56px;font-family:"Indie Flower",cursive;color:var(--white);line-height:1.1}
  .headline--bring{font-size:31px}
  .headline__big{font-size:36px;display:block}
  .headline__small{font-size:24px;display:block;line-height:1.15}

  .greeting{position:absolute;left:49px;top:261px;font-size:12px;font-weight:700}
  .email--bring .greeting{color:var(--sky-deep)}
  .email--welcome .greeting{color:var(--orange)}
  .body-copy{position:absolute;left:49px;top:290px;width:390px;font-size:12.4px;line-height:14px}

  .checklist{position:absolute;left:50px;top:378px;list-style:none;font-size:12.4px}
  .checklist li{display:flex;align-items:center;gap:6px;height:17.3px}
  .checklist svg{width:12px;height:12px}

  .tagline{position:absolute;left:179px;top:362px;font-family:"Indie Flower",cursive;font-size:25px;line-height:30px;color:var(--orange)}

  .cta{position:absolute;display:flex;align-items:center;justify-content:center;width:135px;height:38px;
    font-weight:700;font-size:13px;color:var(--white);text-decoration:none;letter-spacing:.2px}
  .cta--orange{left:50px;top:492px;background:var(--orange);border-bottom:4px solid var(--sky)}
  .cta--blue{left:246px;top:453px;background:var(--sky);border-bottom:4px solid var(--green)}
</style>
</head>
<body>
  <div class="sheet-header"><strong>BLOOM EARLY LEARNING CENTER</strong> &nbsp;|&nbsp; EMAIL MARKETING 2/3</div>
  <div class="sheet-rule"></div>

  <!-- Template: things to bring -->
  <section class="email email--bring">
    <svg class="email__art" viewBox="0 0 476 766" xmlns="http://www.w3.org/2000/svg">
      <defs>
        <linearGradient id="deskTones" x1="0" y1="0" x2="1" y2="1">
          <stop offset="0" stop-color="#d9d6cf"/><stop offset=".6" stop-color="#b89a7a"/><stop offset="1" stop-color="#7a5a3c"/>
        </linearGradient>
        <linearGradient id="classroomTones" x1="0" y1="0" x2="1" y2="1">
          <stop offset="0" stop-color="#c9c2b0"/><stop offset=".45" stop-color="#9bbf55"/><stop offset="1" stop-color="#5a4a3a"/>
        </linearGradient>
      </defs>
      <path d="M200 0H476V108C440 180 360 212 290 208C235 204 238 120 200 0Z" fill="var(--sky)"/>
      <rect x="18" y="20" width="440" height="728" fill="none" stroke="var(--orange)" stroke-width="1" stroke-dasharray="4 3"/>
      <path d="M0 712C60 660 110 600 150 548C190 620 240 700 290 766H0Z" fill="url(#deskTones)" role="img" aria-label="Photo of an apple on a stack of books with coloured pencils"/>
      <path d="M156 550C240 585 390 560 476 462V766H306C270 705 210 630 156 550Z" fill="url(#classroomTones)" role="img" aria-label="Photo of a young girl drawing at a classroom table"/>
    </svg>

    <div class="brand"><span class="brand__dot"></span><span class="brand__name">Bloom Early<br>Learning Center</span></div>
    <h1 class="headline headline--bring">THINGS YOU<br>SHOULD BRING</h1>

    <p class="greeting">Dear Name Surname,</p>
    <p class="body-copy">Lorem ipsum dolor sit amet, consectetur adipiscing elit, sed do eiusmod tempor incididunt ut labore et dolore magna aliqua. Ut enim ad minim veniam, quis nostrud exercitation ullamco laboris nisi ut aliquip ex ea commodo consequat. Duis aute irure dolor in reprehenderit in voluptate velit esse cillum dolore eu fugiat nulla pariatur.</p>
    <ul class="checklist">
      <li><svg viewBox="0 0 12 12"><path d="M1 6.5L4.5 10L11 1" fill="none" stroke="var(--sky-deep)" stroke-width="1.6"/></svg>Lorem ipsum dolor sit amet</li>
      <li><svg viewBox="0 0 12 12"><path d="M1 6.5L4.5 10L11 1" fill="none" stroke="var(--sky-deep)" stroke-width="1.6"/></svg>Duis aute irure dolor in reprehenderit in voluptate</li>
      <li><svg viewBox="0 0 12 12"><path d="M1 6.5L4.5 10L11 1" fill="none" stroke="var(--sky-deep)" stroke-width="1.6"/></svg>Ut enim ad minim veniam</li>
      <li><svg viewBox="0 0 12 12"><path d="M1 6.5L4.5 10L11 1" fill="none" stroke="var(--sky-deep)" stroke-width="1.6"/></svg>sed do eiusmod tempor incididunt ut labore et dolore</li>
      <li><svg viewBox="0 0 12 12"><path d="M1 6.5L4.5 10L11 1" fill="none" stroke="var(--sky-deep)" stroke-width="1.6"/></svg>esse cillum dolore eu fugiat nulla</li>
    </ul>
    <a class="cta cta--orange" href="#">VISIT BLOOM</a>
  </section>

  <!-- Template: welcome -->
  <section class="email email--welcome">
    <svg class="email__art" viewBox="0 0 476 766" xmlns="http://www.w3.org/2000/svg">
      <defs>
        <linearGradient id="staffTones" x1="0" y1="0" x2="1" y2="1">
          <stop offset="0" stop-color="#e46aa0"/><stop offset=".35" stop-color="#7a5a48"/><stop offset=".7" stop-color="#9bcb3c"/><stop offset="1" stop-color="#c8d96a"/>
        </linearGradient>
        <linearGradient id="playroomTones" x1="0" y1="0" x2="1" y2="1">
          <stop offset="0" stop-color="#8a9a6a"/><stop offset=".5" stop-color="#8c8f96"/><stop offset="1" stop-color="#c24a3a"/>
        </linearGradient>
        <linearGradient id="danceTones" x1="0" y1="0" x2="1" y2="1">
          <stop offset="0" stop-color="#e9ece6"/><stop offset=".5" stop-color="#e8763a"/><stop offset="1" stop-color="#b9b6b0"/>
        </linearGradient>
      </defs>
      <path d="M201 0H476V100C430 175 340 212 260 208C215 206 215 100 201 0Z" fill="var(--orange)"/>
      <rect x="17" y="20" width="441" height="728" fill="none" stroke="var(--sky)" stroke-width="1" stroke-dasharray="4 3"/>
      <path d="M0 372C100 395 220 470 262 548C200 528 90 538 0 572Z" fill="url(#staffTones)" role="img" aria-label="Photo of a caregiver holding a toddler in a bright classroom"/>
      <path d="M0 576C90 544 200 534 262 552C225 604 210 690 229 766H0Z" fill="url(#playroomTones)" role="img" aria-label="Photo of a little boy playing with toy cars on a rug"/>
      <path d="M233 766C214 680 232 594 272 554C342 534 432 474 476 348V766Z" fill="url(#danceTones)" role="img" aria-label="Photo of a little girl in an orange dress dancing among confetti"/>
    </svg>

    <div class="brand"><span class="brand__dot"></span><span class="brand__name">Bloom Early<br>Learning Center</span></div>
    <h1 class="headline">
      <span class="headline__big">WELCOME</span>
      <span class="headline__small">to Bloom Early<br>Learning Center</span>
    </h1>

    <p class="greeting">Dear Name Surname,</p>
    <p class="body-copy">Bloom Early Learning Center creates the ideal environment for kids to feel safe, loved, and accepted as they try new ideas, develop academic skills and imitate adult roles. We learn through play and believe that play makes it possible for children to learn social skills and develop friendships.</p>
    <p class="tagline">We love to have<br>you on board!</p>
    <a class="cta cta--blue" href="#">VISIT BLOOM</a>
  </section>
</body>
</html>
```